Landing Page Design

Require a landing page design.

A wire concept has been provided along with a relevant logo and image files.

Target Market(s)

Facilities/Property Management companies
Maintenance Managers for manufacturing and related sites
Personal Assistants (those given responsible for the maintenance and cleaning of commercial properties

Industry/Entity Type

Construction

Number of Pages Required

1 page

Requirements
Must have
• 1. Layout as per wire design concept
2. Stick to colour scheme of logo and include plenty of white space
Should not have
• No flash

```html
<!DOCTYPE html>
<html lang="en">
<head>
<meta charset="utf-8">
<title>Norvale Property Services Group – Free Window &amp; Carpet Clean</title>
<link rel="stylesheet" href="https://fonts.googleapis.com/css2?family=PT+Serif:wght@400;700&family=Noto+Sans:wght@400;700&display=swap">
<style>
  :root {
    --navy: #0b3f8a;
    --navy-deep: #062c66;
    --blue: #1a5fb4;
    --blue-light: #2b73c9;
    --green: #5a9a2a;
    --green-dark: #3f7a1c;
    --green-light: #7cb342;
    --ink: #1a1a1a;
    --text-blue: #0d3f87;
    --field: #dcdcdc;
    --field-border: #9a9a9a;
    --panel: #efefef;
    --white: #ffffff;
    --sky: #8fc4ef;
    --glass: #2d5a86;
    --hedge: #4f7d2a;
  }
  * { box-sizing: border-box; margin: 0; padding: 0; }
  html, body { width: 1046px; height: 1200px; overflow: hidden; background: var(--white); }
  body { position: relative; font-family: "Noto Sans", sans-serif; color: var(--ink); }

  .site-header { position: absolute; left: 0; top: 0; width: 1046px; height: 130px; background: var(--white); border-bottom: 4px solid var(--green); }
  .brand { position: absolute; left: 22px; top: 16px; width: 306px; height: 100px; background: linear-gradient(180deg, var(--blue) 0%, var(--navy-deep) 100%); display: flex; align-items: center; gap: 12px; padding-left: 20px; }
  .brand-square { width: 34px; height: 34px; background: var(--white); }
  .brand-name { font-family: "Noto Sans", sans-serif; font-weight: 700; font-size: 34px; color: var(--white); letter-spacing: 1px; line-height: 1; }

  .hero { position: absolute; left: 0; top: 130px; width: 1046px; height: 291px; background: linear-gradient(160deg, #1c5cb0 0%, var(--navy) 55%, var(--navy-deep) 100%); overflow: hidden; }
  .hero-photo { position: absolute; left: 0; top: 0; }
  .hero-title { position: absolute; left: 22px; top: 56px; font-family: "PT Serif", serif; font-weight: 700; font-size: 44px; line-height: 57px; color: var(--white); text-shadow: 2px 2px 3px rgba(0,0,0,.45); }
  .hero-call { position: absolute; left: 22px; top: 216px; font-family: "PT Serif", serif; font-weight: 700; font-size: 28px; color: var(--white); text-shadow: 1px 1px 2px rgba(0,0,0,.45); }

  .tagline-band { position: absolute; left: 0; top: 421px; width: 1046px; height: 60px; background: linear-gradient(180deg, var(--green-light) 0%, var(--green) 50%, var(--green-dark) 100%); padding-left: 22px; display: flex; align-items: center; font-family: "PT Serif", serif; font-weight: 700; font-size: 21px; color: var(--white); text-shadow: 1px 1px 2px rgba(0,0,0,.4); }

  .main-copy { position: absolute; left: 24px; top: 516px; width: 590px; font-size: 12.5px; line-height: 17px; }
  .lead { color: var(--text-blue); font-weight: 700; font-size: 13.5px; line-height: 18px; margin-bottom: 14px; }
  .main-copy p { margin-bottom: 16px; }
  .reasons-title { color: var(--text-blue); font-weight: 700; font-size: 13.5px; margin-top: 28px; margin-bottom: 10px; }
  .reasons { list-style: none; }
  .reasons li { position: relative; padding-left: 14px; margin-bottom: 12px; }
  .reasons li::before { content: ""; position: absolute; left: 1px; top: 7px; width: 5px; height: 5px; border-radius: 50%; background: var(--ink); }

  .cta-row { position: absolute; left: 120px; top: 950px; display: flex; gap: 76px; }
  .cta-button { width: 140px; height: 93px; border-radius: 4px; background: linear-gradient(180deg, var(--blue-light) 0%, var(--navy) 60%, var(--navy-deep) 100%); box-shadow: inset 0 0 0 2px #4c8fdc; display: flex; align-items: center; justify-content: center; text-align: center; font-family: "PT Serif", serif; font-weight: 700; font-size: 19px; line-height: 21px; color: var(--white); text-shadow: 1px 1px 2px rgba(0,0,0,.5); }
  .closing { position: absolute; left: 24px; top: 1066px; width: 590px; font-weight: 700; font-size: 13px; line-height: 18px; }

  .divider { position: absolute; left: 619px; top: 504px; height: 618px; border-left: 2px dotted #c8c8c8; }

  .enquiry { position: absolute; left: 668px; top: 518px; width: 333px; height: 413px; background: var(--panel); border: 1px solid #b8b8b8; border-radius: 4px; overflow: hidden; }
  .enquiry-head { height: 106px; background: linear-gradient(180deg, var(--blue-light) 0%, var(--navy) 55%, var(--navy-deep) 100%); text-align: center; color: var(--white); font-family: "PT Serif", serif; font-weight: 700; font-size: 16.5px; line-height: 20px; padding-top: 9px; text-shadow: 1px 1px 2px rgba(0,0,0,.4); }
  .enquiry-head .phone { font-size: 28px; line-height: 30px; }
  .enquiry-head .phone small { font-size: 16.5px; }
  .enquiry-form { padding: 6px 12px 0 12px; }
  .field-label { display: block; font-weight: 700; font-size: 12.5px; margin-bottom: 4px; }
  .field { display: block; width: 100%; height: 36px; background: var(--field); border: 1px solid var(--field-border); border-radius: 3px; margin-bottom: 10px; }
  .submit { display: block; margin: 8px auto 0; width: 154px; height: 28px; border-radius: 4px; border: 1px solid #4c8fdc; background: linear-gradient(180deg, var(--blue-light) 0%, var(--navy-deep) 100%); color: var(--white); font-family: "Noto Sans", sans-serif; font-weight: 700; font-size: 12.5px; letter-spacing: .5px; }

  .testimonials { position: absolute; left: 668px; top: 951px; width: 333px; height: 174px; border-radius: 4px; background: linear-gradient(180deg, var(--blue-light) 0%, var(--navy) 50%, var(--navy-deep) 100%); border: 1px solid #4c8fdc; color: var(--white); padding: 8px 12px; }
  .testimonials h2 { font-family: "PT Serif", serif; font-weight: 700; font-size: 22px; line-height: 24px; letter-spacing: .5px; }
  .testimonials blockquote { font-size: 12px; line-height: 16px; margin-top: 2px; }
  .testimonials cite { display: block; font-style: normal; font-weight: 700; font-size: 12.5px; }
  .testimonials .more { position: absolute; right: 16px; bottom: 8px; font-weight: 700; font-size: 13px; color: var(--white); text-decoration: underline; }

  .site-footer { position: absolute; left: 0; top: 1138px; width: 1046px; height: 62px; background: linear-gradient(180deg, var(--blue) 0%, var(--navy-deep) 100%); color: var(--white); font-size: 12.5px; padding-left: 24px; display: flex; align-items: center; }
  .site-footer strong { margin-left: 4px; }
</style>
</head>
<body>
  <header class="site-header">
    <div class="brand"><span class="brand-square"></span><span class="brand-name">NORVALE</span></div>
  </header>

  <section class="hero">
    <svg class="hero-photo" width="1046" height="291" viewBox="0 0 1046 291" role="img" aria-label="Photo of window cleaners on ladders washing the glass facade of an office building behind a hedge">
      <defs>
        <linearGradient id="photoTone" x1="0" y1="0" x2="0" y2="1">
          <stop offset="0" stop-color="#a9d3f2"/>
          <stop offset="0.2" stop-color="#6f9fc8"/>
          <stop offset="0.65" stop-color="#2d5a86"/>
          <stop offset="0.8" stop-color="#4f7d2a"/>
          <stop offset="1" stop-color="#3a6620"/>
        </linearGradient>
      </defs>
      <path d="M694 0 H1046 V291 H584 C625 200 665 100 694 0 Z" fill="url(#photoTone)"/>
      <path d="M694 0 C665 100 625 200 584 291" fill="none" stroke="#ffffff" stroke-width="4"/>
    </svg>
    <h1 class="hero-title">FREE WINDOW<br>&amp; CARPET CLEAN</h1>
    <p class="hero-call">Call Now on 1300 55 01 87</p>
  </section>

  <div class="tagline-band">No Contracts – Routine Office Cleaning – Painless Experience</div>

  <main class="main-copy">
    <p class="lead">Engage our routine office cleaning for at least 6 months and receive a FREE Carpet and Window clean &nbsp;&nbsp;No strings attached, no contracts.</p>
    <p class="lead">To take advantage of this great offer call us on 1300 55 01 87 or complete and submit the form on this page.</p>
    <p>At Norvale we provide all your property service needs - painlessly. We understand that cleaning and other property services should be background activities. A set and forget proposition.</p>
    <p>We also know that you should not have to police or project manage our Service Teams.</p>
    <p>After engaging Norvale, property services will become your lowest priority, as it is our highest priority.</p>
    <h2 class="reasons-title">Top 5 Reasons to Choose Norvale</h2>
    <ul class="reasons">
      <li>We self audit and performance manage our Service Teams while they're on the job</li>
      <li>We minimise contact time required between the client and our Service Teams</li>
      <li>Our Service Teams are proactive in identifying irregular requirements</li>
      <li>We have a comprehensive Health Safety Management system</li>
      <li>We can provide our Property Services on a National basis</li>
    </ul>
  </main>

  <div class="cta-row">
    <a class="cta-button">BOOK A<br>FREE QUOTE</a>
    <a class="cta-button">VISIT OUR<br>WEBSITE</a>
  </div>

  <p class="closing">If you would like to join our growing list of satisfied clients, call NOW to discuss how Norvale can best meet all your Commercial Cleaning and Property Service needs.</p>

  <div class="divider"></div>

  <aside class="enquiry">
    <div class="enquiry-head">
      Take advantage of this great offer.<br>Contact Us Now on<br>
      <span class="phone">1300 55 01 87 <small>or</small></span><br>
      register your interest below
    </div>
    <form class="enquiry-form">
      <label class="field-label">Name</label><span class="field"></span>
      <label class="field-label">Business Name</label><span class="field"></span>
      <label class="field-label">Email</label><span class="field"></span>
      <label class="field-label">Phone</label><span class="field"></span>
      <button class="submit" type="button">SUBMIT</button>
    </form>
  </aside>

  <aside class="testimonials">
    <h2>TESTIMONIALS</h2>
    <blockquote>Lorem Ipsum is simply dummy text of the printing and typesetting industry. Lorem Ipsum has been the industry's standard dummy text ever since the 1500s, when an unknown printer took a galley of type and scrambled it to make a type specimen book.</blockquote>
    <cite>- Dana Whitlow</cite>
    <a class="more">More</a>
  </aside>

  <footer class="site-footer">Copyright of <strong>NORVALE Property Service Group</strong></footer>
</body>
</html>
```